Sports nutritional supplement brand*

We need to design an integrated packaging for a sports nutritional supplement brand containing more than 30 products The design of the packaging consists of two parts, half in black color, fixed in all types, and the other half is variable. I sent you pictures containing some beautiful ideas that suit what I think of. The design must contain a place for the taste image, such as chocolate, strawberry, banana, orange, grape, watermelon The company name must be clearly visible in the middle and the location of the code and barcode

Target Market(s)

the whole world

Industry/Entity Type

Entrepreneur

Font styles to use
Decorative

Colors

Designer to choose colors to be used in the design.

Requirements
Must have
• The project consists of several types of supplements. I need each type to be different from the other in terms of a color that is constant, such as the black color and the half of the box is color changing, for example the box is made of black and red and the second box is black and yellow and the colors must be bright and 3D
Nice to have
• The outer box will be white and the box will be completely wrapped from the head neck down, not around the box There should be a small box design, a large protein box, and a protein pouch bag
Should not have

```html
<!DOCTYPE html>
<html lang="en">
<head>
<meta charset="utf-8">
<title>IRONPEAK Mass Gainer – Strawberry Label</title>
<link href="https://fonts.googleapis.com/css2?family=Orbitron:wght@400;500;700&family=Montserrat:wght@400;500&display=swap" rel="stylesheet">
<style>
  :root {
    --backdrop: #cdd5da;
    --panel-black: #0b0b0c;
    --panel-black-soft: #1a1a1c;
    --accent-red: #e41e26;
    --bar-brown: #5a3026;
    --silver: #d6d6d8;
    --text-light: #e6e6e6;
    --text-muted: #7c7c80;
    --berry-dark: #2a0508;
    --berry-mid: #6e0e14;
    --leaf: #1f3a1c;
    --white: #ffffff;
  }
  * { box-sizing: border-box; margin: 0; padding: 0; }
  html, body { width: 1200px; height: 900px; overflow: hidden; }
  body { background: var(--backdrop); position: relative; font-family: "Montserrat", sans-serif; }

  .label {
    position: absolute; left: 155px; top: 20px; width: 890px; height: 860px;
    background: var(--white);
  }

  /* variable flavour panel */
  .flavour-panel {
    position: absolute; left: 0; top: 0; width: 276px; height: 860px; overflow: hidden;
  }
  .flavour-photo {
    position: absolute; inset: 0;
    background:
      radial-gradient(circle at 45% 40%, var(--berry-mid) 0%, transparent 45%),
      radial-gradient(circle at 60% 75%, var(--berry-mid) 0%, transparent 40%),
      radial-gradient(circle at 30% 15%, var(--leaf) 0%, transparent 30%),
      linear-gradient(180deg, var(--berry-dark), #3d070c 50%, var(--berry-dark));
  }
  .info-tag {
    position: absolute; left: 77px; top: 140px; width: 113px; height: 163px;
    border: 1px solid var(--white); border-radius: 4px;
    clip-path: polygon(0 0, 100% 0, 100% 78%, 78% 100%, 0 100%);
    background: rgba(0,0,0,0.15);
  }
  .info-tag__head { height: 18px; background: var(--white); }
  .info-tag__text {
    padding: 6px 10px; color: var(--white); font-size: 6px; line-height: 1.3;
  }
  .flavour-name {
    position: absolute; left: 206px; top: 501px; width: 20px; height: 304px;
    border: 1px solid var(--white); border-radius: 4px;
    display: flex; align-items: center; justify-content: center;
  }
  .flavour-name span {
    transform: rotate(-90deg); white-space: nowrap;
    font-family: "Orbitron", sans-serif; font-size: 15px; letter-spacing: 1px; color: var(--white);
  }
  .flavour-name b { font-weight: 400; color: var(--silver); }
  .capsule-count { position: absolute; left: 42px; top: 743px; display: flex; align-items: flex-end; gap: 6px; }
  .capsule-count__icon { width: 48px; height: 64px; background: rgba(255,255,255,0.12); border-radius: 3px; }
  .capsule-count__figures { color: var(--white); font-family: "Orbitron", sans-serif; line-height: 1; }
  .capsule-count__number { font-size: 44px; font-weight: 400; letter-spacing: 1px; }
  .capsule-count__unit { font-size: 12px; letter-spacing: 1px; }

  .panel-divider { position: absolute; left: 276px; top: 0; width: 4px; height: 860px; background: var(--white); }

  /* fixed black panel */
  .core-panel {
    position: absolute; left: 280px; top: 0; width: 610px; height: 860px;
    background: radial-gradient(ellipse at 60% 30%, var(--panel-black-soft), var(--panel-black) 70%);
    color: var(--text-light);
  }
  .brand {
    position: absolute; left: 68px; top: 200px; display: flex; align-items: center; gap: 14px;
  }
  .brand__name {
    font-family: "Orbitron", sans-serif; font-weight: 700; font-size: 58px; letter-spacing: 2px; color: var(--silver);
  }
  .brand__square { width: 22px; height: 22px; background: var(--accent-red); }
  .brand-tag {
    position: absolute; left: 94px; top: 280px; width: 181px; height: 20px;
    background: var(--accent-red); color: var(--white);
    font-family: "Orbitron", sans-serif; font-size: 9.5px; letter-spacing: 0.3px;
    display: flex; align-items: center; justify-content: center;
    clip-path: polygon(0 0, 100% 0, 96% 100%, 3% 100%);
  }
  .product-type {
    position: absolute; left: 344px; top: 279px;
    font-family: "Orbitron", sans-serif; font-size: 17px; letter-spacing: 0.5px; color: var(--white);
  }
  .product-type em { font-style: normal; color: var(--accent-red); }

  .nutrient { position: absolute; left: 70px; width: 340px; height: 41px; display: flex; align-items: stretch;
    background: linear-gradient(90deg, var(--bar-brown), rgba(90,48,38,0.5) 60%, transparent); }
  .nutrient--protein { top: 407px; }
  .nutrient--creatine { top: 489px; }
  .nutrient--vitamin { top: 571px; }
  .nutrient__amount {
    background: var(--accent-red); color: var(--white); font-family: "Orbitron", sans-serif;
    display: flex; align-items: flex-end; padding: 0 8px 4px 12px; line-height: 1;
  }
  .nutrient--protein .nutrient__amount { width: 76px; }
  .nutrient--creatine .nutrient__amount, .nutrient--vitamin .nutrient__amount { width: 56px; }
  .nutrient__amount strong { font-size: 32px; font-weight: 400; }
  .nutrient__amount small { font-size: 10px; margin-left: 2px; }
  .nutrient__label { padding: 6px 0 0 12px; font-family: "Orbitron", sans-serif; line-height: 1.05; }
  .nutrient__name { font-size: 16px; color: var(--text-light); }
  .nutrient__unit { font-size: 10px; color: var(--text-light); }

  .details { position: absolute; left: 70px; top: 655px; width: 230px; }
  .details__title { font-family: "Orbitron", sans-serif; font-size: 13px; color: var(--text-muted); margin-bottom: 8px; }
  .details__body { font-size: 6px; line-height: 1.45; color: var(--text-muted); }
  .net-weight { position: absolute; left: 72px; top: 767px; font-family: "Orbitron", sans-serif; font-size: 14px; color: var(--text-light); }
  .net-note { position: absolute; left: 72px; top: 789px; width: 250px; font-size: 5.5px; line-height: 1.4; color: var(--text-muted); }
  .code-area { position: absolute; left: 520px; top: 738px; width: 200px; height: 84px; background: var(--white); border-radius: 2px; }
  .core-panel .code-area { left: 240px; }
</style>
</head>
<body>
  <main class="label">
    <section class="flavour-panel">
      <div class="flavour-photo" role="img" aria-label="Close-up photograph of ripe strawberries"></div>
      <div class="info-tag">
        <div class="info-tag__head"></div>
        <p class="info-tag__text">Lorem ipsum dolor sit amet, consectetuer adipiscing elit, sed diam nonummy nibh euismod tincidunt ut laoreet dolore magna aliquam erat volutpat. Ut wisi enim ad minim veniam, quis nostrud exerci tation ullamcorper suscipLorem ipsum dolor sit amet, consectetuer adipiscing elit.</p>
      </div>
      <div class="flavour-name"><span>STRAWBERRY <b>FLAVOUR</b></span></div>
      <div class="capsule-count">
        <div class="capsule-count__icon" role="img" aria-label="Athlete pictogram"></div>
        <div class="capsule-count__figures">
          <div class="capsule-count__number">90</div>
          <div class="capsule-count__unit">CAPSULES</div>
        </div>
      </div>
    </section>

    <div class="panel-divider"></div>

    <section class="core-panel">
      <div class="brand">
        <span class="brand__name">IRONPEAK</span>
        <span class="brand__square"></span>
      </div>
      <div class="brand-tag">DIETERY SUPPLIMENT</div>
      <div class="product-type">MASS <em>GAINER</em></div>

      <div class="nutrient nutrient--protein">
        <div class="nutrient__amount"><strong>25</strong><small>g</small></div>
        <div class="nutrient__label"><div class="nutrient__name">PROTEIN</div><div class="nutrient__unit">per spoon</div></div>
      </div>
      <div class="nutrient nutrient--creatine">
        <div class="nutrient__amount"><strong>8</strong><small>g</small></div>
        <div class="nutrient__label"><div class="nutrient__name">CREATINE</div><div class="nutrient__unit">per spoon</div></div>
      </div>
      <div class="nutrient nutrient--vitamin">
        <div class="nutrient__amount"><strong>3</strong><small>g</small></div>
        <div class="nutrient__label"><div class="nutrient__name">VITAMINE</div><div class="nutrient__unit">per spoon</div></div>
      </div>

      <div class="details">
        <h2 class="details__title">Lorem ipsum</h2>
        <p class="details__body">LoLorem ipsum dolor sit amet, consectetuer adipiscing elit, sed diam nonummy nibh euismod tincidunt ut laoreet dolore magna aliquam erat volutpat. Ut wisi enim ad minim veniam, quis nostrud exerci tation ullamcorper suscipit lobortis nisl ut aliquip ex ea commodo consequat. Duis autem vel eum iriure dolor in hendrerit in vulputate velit esse</p>
      </div>
      <div class="net-weight">NET WEIGHT : 2kg</div>
      <p class="net-note">Lorem ipsum dolor sit amet, consectetuer adipiscing elit, sed diam nonummy nibh euismod tincidunt ut laoreet dolore magna aliquam erat volutpat. Ut wisi enim ad minim veniam, quis nostrud exerci tation ullamcorper suscip</p>
      <div class="code-area"></div>
    </section>
  </main>
</body>
</html>
```